Web re-design project www.vempresoft.com

We need a corporate website for a startup company called Vempre Labs. The company offers web-based worksite management system for big construction companies. In short, replacing annoying papers with iPads.
We need the site main page to provide basic overview of the company and then inner page layout for displaying news and detailed information about products.
Currently we have a site up at:
http://www.vempresoft.com/en/main
but as you can see the graphic design is a bit lacking in quality(implemented by a tech guy :)
We need you to pimp that web site design up!
There is possibility for more freelance work in the future related to our web products, slide show designs and printed marketing materials.
Our main product is LOMVI. You can find a short presentation about what it does here:
http://www.vempresoft.com/en/lomvi
Here you can find packages of images and screenshots related to our company:
https://files.plimbox.net/u/7719026/vempre_images.zip
https://files.plimbox.net/u/7719026/vempresoft%20images2.zip
Product logo svg can be found here:
https://files.plimbox.net/u/7719026/LOMVI-logo.svg
Your are not forced to use those images, but hopefully there will be something that is useful.
Hope to hear from you guys soon!
Cheers,
Ossi
Update:
We will be using LOMVI logo as the company brand. I don't like our current Vempre Labs company logo, so that doesn't need to be included in the site design.
Update 2:
I like website designs that are "light", elegant and pretty simplistic. One example is our product login page (screenshot included in files).
Update 3:
Sites from the same industry / type of products:
http://www.rakmoda.fi/
http://www.quarvelgrid.com/products/software/network-applications/fieldsync-3d
http://www.dornvex.com/construction/heavy-civil/software-solutions/Linked-Network.aspx?dtID=overview&
Target audience for the website is companies in the construction sector, and possibly corporate investors
Graphic Design

```html
<!DOCTYPE html>
<html lang="en">
<head>
<meta charset="utf-8">
<title>LOMVI – Vempre Labs</title>
<link rel="stylesheet" href="https://fonts.googleapis.com/css2?family=Figtree:wght@400;600;800&display=swap">
<style>
:root{
  --ink:#1c1c1c;
  --text:#555049;
  --taupe:#8f8675;
  --taupe-dark:#7a7162;
  --sand:#e0d6ca;
  --sand-line:#cfc4b6;
  --tab:#cdc1b2;
  --tab-fold:#b3a795;
  --headline:#c4b8a6;
  --nav-text:#7d7464;
  --rule:#eeeae5;
  --white:#ffffff;
  --dot:#d3cabe;
  --dot-active:#5e4a42;
  --accent:#e03a2f;
}
*{box-sizing:border-box;margin:0;padding:0}
html,body{width:987px;height:1200px;overflow:hidden;background:var(--white)}
body{position:relative;font-family:"Figtree",Arial,sans-serif;color:var(--text)}
a{color:inherit;text-decoration:none}

.brand{position:absolute;left:66px;top:30px;display:flex;align-items:center;gap:16px}
.brand-dot{width:14px;height:14px;border-radius:50%;background:var(--accent)}
.brand-name{font-size:50px;font-weight:400;color:var(--ink);letter-spacing:1px;line-height:1}

.main-nav{position:absolute;left:65px;top:115px;width:860px;height:40px;border-top:1px solid var(--rule);border-bottom:1px solid var(--rule)}
.main-nav ul{list-style:none;position:absolute;left:148px;top:1px;display:flex;height:37px}
.main-nav li{height:37px;display:flex;align-items:center;justify-content:center;font-size:18px;font-weight:600;color:var(--nav-text)}
.main-nav li+li{border-left:1px solid var(--rule)}
.main-nav li:nth-child(1){width:145px}
.main-nav li:nth-child(2){width:144px}
.main-nav li:nth-child(3){width:137px}
.main-nav li:nth-child(4){width:160px}
.main-nav li.is-current{background:var(--taupe);color:var(--white)}

.slider{position:absolute;left:60px;top:193px;width:867px;height:435px;background:var(--sand);border:1px solid var(--sand-line)}
.slide-card{position:absolute;left:19px;top:20px;width:830px;height:395px;background:var(--white);box-shadow:0 1px 3px rgba(0,0,0,.15)}
.slide-photo{position:absolute;left:15px;top:13px;width:800px;height:369px;background:linear-gradient(110deg,#c9d23a 0%,#3d3b4a 28%,#8a7a6e 45%,#9a7f72 70%,#a5918a 100%)}
.slide-dots{position:absolute;left:377px;top:419px;display:flex;gap:13.5px}
.slide-dots span{width:10px;height:10px;border-radius:50%;background:var(--dot)}
.slide-dots span.is-active{background:var(--dot-active)}

.slider-arrow{position:absolute;top:352px;width:49px;height:81px}
.slider-arrow.prev{left:35px}
.slider-arrow.next{left:902px}

.intro-title{position:absolute;left:60px;top:664px;width:867px;text-align:center;font-size:27px;font-weight:800;line-height:33.5px;color:var(--headline)}
.intro-text{position:absolute;left:60px;top:790px;width:867px;text-align:center;font-size:15.4px;line-height:19.3px;color:var(--text)}

.site-footer{position:absolute;left:0;top:985px;width:987px;height:215px;background:var(--taupe);color:var(--white)}
.footer-col{position:absolute;top:24px}
.footer-col h3{font-size:15px;font-weight:600;line-height:19px;margin-bottom:2px;margin-left:2px}
.footer-col li{list-style:none;font-size:15px;line-height:19.3px}
.col-about{left:58px}
.col-services{left:237px}
.col-guidance{left:416px}
.col-social{left:613px}
.col-contact{left:812px}
.social-links{display:flex;gap:6px;margin-top:9px}
.social-links span{width:34px;height:34px;background:var(--taupe-dark);border:1px solid #a59c8b;border-radius:3px}
.assist{position:absolute;left:0;top:155px;width:987px;text-align:center;font-size:15px;line-height:21px;display:flex;justify-content:center;align-items:center;gap:10px}
.assist svg{width:14px;height:14px}
.copyright{position:absolute;left:0;top:177px;width:987px;text-align:center;font-size:15px;font-weight:600;line-height:21px}
</style>
</head>
<body>

<header>
  <a class="brand" href="#"><span class="brand-dot"></span><span class="brand-name">LOMVI</span></a>
  <nav class="main-nav">
    <ul>
      <li class="is-current">Home</li>
      <li>Products</li>
      <li>News</li>
      <li>Contact</li>
    </ul>
  </nav>
</header>

<section class="slider">
  <div class="slide-card">
    <div class="slide-photo" role="img" aria-label="Site engineer in a hard hat and high-visibility jacket checking a tablet on a road construction site with an excavator behind"></div>
  </div>
  <div class="slide-dots"><span></span><span class="is-active"></span><span></span><span></span><span></span><span></span></div>
</section>

<svg class="slider-arrow prev" viewBox="0 0 49 81" aria-label="Previous slide">
  <polygon points="0,17 25,0 25,17" fill="var(--tab-fold)"/>
  <rect x="0" y="17" width="49" height="64" fill="var(--tab)"/>
  <polygon points="14,49 32,38 32,60" fill="var(--white)"/>
</svg>
<svg class="slider-arrow next" viewBox="0 0 49 81" aria-label="Next slide">
  <polygon points="49,17 24,0 24,17" fill="var(--tab-fold)"/>
  <rect x="0" y="17" width="49" height="64" fill="var(--tab)"/>
  <polygon points="35,49 17,38 17,60" fill="var(--white)"/>
</svg>

<main>
  <h1 class="intro-title">LOMVI is a cloud-based service for road construction projects<br>and<br>it's going full steam!</h1>
  <p class="intro-text">This is Photoshop's version &nbsp;of Lorem Ipsum. Proin gravida nibh vel velit auctor aliquet. Aenean sollicitudin, lorem quis<br>bibendum auctor, nisi elit consequat ipsum, nec sagittis sem nibh id elit. Duis sed odio sit amet nibh vulputate cursus a<br>sit amet mauris. Morbi accumsan ipsum velit. Nam nec tellus a odio tincidunt auctor a ornare odio. Sed non &nbsp;mauris vitae<br>erat consequat auctor eu in elit. Class aptent taciti sociosqu ad litora torquent per conubia nostra, per inceptos hime-<br>naeos. Mauris in erat justo. Nullam ac urna eu felis dapibus condimentum sit amet a augue. Sed non neque elit. Sed ut<br>imperdiet nisi. Proin condimentum fermentum nunc. Etiam pharetra, erat sed fermentum feugiat, velit mauris egestas<br>quam, ut aliquam massa nisl quis neque. Suspendisse in orci enim.</p>
</main>

<footer class="site-footer">
  <div class="footer-col col-about">
    <h3>About us</h3>
    <ul><li>Company info</li><li>The Team</li><li>Careers</li><li>Privacy Policy</li></ul>
  </div>
  <div class="footer-col col-services">
    <h3>Services</h3>
    <ul><li>Structural Steels</li><li>Roofs</li><li>Walls</li><li>Foundations</li></ul>
  </div>
  <div class="footer-col col-guidance">
    <h3>Design Guidance</h3>
    <ul><li>Structural design</li><li>Flooring</li><li>Steel bridges</li><li>Envelope</li></ul>
  </div>
  <div class="footer-col col-social">
    <h3>Social Media</h3>
    <ul><li>Follow us on</li></ul>
    <div class="social-links" aria-label="Social media links"><span></span><span></span><span></span><span></span></div>
  </div>
  <div class="footer-col col-contact">
    <h3>Contact</h3>
    <ul><li>Partners</li><li>Contact</li><li>Site Map</li><li>Location</li></ul>
  </div>
  <p class="assist">For assistance
    <svg viewBox="0 0 14 14" aria-hidden="true"><path d="M3 1h2.5l1 3-1.5 1.2a8 8 0 0 0 3.8 3.8L10 7.5l3 1V11a1.5 1.5 0 0 1-1.5 1.5A10.5 10.5 0 0 1 1.5 2.5 1.5 1.5 0 0 1 3 1z" fill="#5ec3ea"/></svg>
    <span>1-800-555-0142</span></p>
  <p class="copyright">Copyright © Vempre Labs 2012</p>
</footer>

</body>
</html>
```